Personal Training

Personal Fitness Trainer
Sports Nutritionist
Individual and Group rates available
Certifications
Global Wellness Coaching Federation
Continental Athletic Studies Council

Industry/Entity Type

Fitness

Contact Information for Business Card

Dorinda Pellham
555-284-7163
vetrubel4@quintmail.example

```html
<!DOCTYPE html>
<html lang="en">
<head>
<meta charset="utf-8">
<title>Dorinda Pellham — Personal Training Business Card</title>
<link rel="stylesheet" href="https://fonts.googleapis.com/css2?family=Arimo:wght@400&family=Great+Vibes&display=swap">
<style>
  :root {
    --page-bg: #e9e7e3;
    --card-white: #ffffff;
    --brand-blue: #4a78cf;
    --brand-blue-dark: #2f5bb5;
    --text-dark: #2b2b2b;
    --text-grey: #4d4d4d;
    --dot-blue: #8aa6dc;
    --photo-light: #d9d4dc;
    --photo-dark: #5b4a6a;
  }
  * { margin: 0; padding: 0; box-sizing: border-box; }
  html, body { width: 1200px; height: 885px; overflow: hidden; }
  body { background: var(--page-bg); position: relative; font-family: "Arimo", Arial, sans-serif; }

  .card {
    position: absolute;
    width: 540px;
    height: 309px;
    background: var(--card-white);
    box-shadow: 0 6px 18px rgba(0,0,0,0.18);
    overflow: hidden;
  }
  .card-front { left: 50px; top: 120px; }
  .card-back { left: 610px; top: 456px; }

  .front-art { position: absolute; inset: 0; width: 540px; height: 309px; }

  .contact {
    position: absolute;
    right: 28px;
    top: 22px;
    text-align: right;
  }
  .contact-name {
    font-family: "Great Vibes", cursive;
    font-size: 38px;
    line-height: 1;
    color: var(--brand-blue);
    font-weight: 400;
  }
  .contact-phone { font-size: 15px; color: var(--text-dark); margin-top: 6px; }
  .contact-email { font-size: 15px; color: var(--brand-blue); margin-top: 14px; }

  .services {
    position: absolute;
    right: 28px;
    top: 150px;
    list-style: none;
    text-align: right;
  }
  .services li {
    font-size: 13px;
    line-height: 21px;
    color: var(--text-grey);
    display: flex;
    justify-content: flex-end;
    align-items: center;
    gap: 10px;
  }
  .services li::after {
    content: "";
    width: 6px;
    height: 6px;
    border-radius: 50%;
    background: var(--dot-blue);
    flex: none;
  }

  .back-name {
    position: absolute;
    inset: 0;
    display: flex;
    align-items: center;
    justify-content: center;
    font-family: "Great Vibes", cursive;
    font-size: 80px;
    color: var(--brand-blue);
    font-weight: 400;
  }
</style>
</head>
<body>
  <section class="card card-front">
    <svg class="front-art" viewBox="0 0 540 309" aria-hidden="false">
      <defs>
        <linearGradient id="photoTone" x1="0" y1="0" x2="0.3" y2="1">
          <stop offset="0" stop-color="var(--photo-light)"/>
          <stop offset="0.6" stop-color="#b7aebd"/>
          <stop offset="1" stop-color="var(--photo-dark)"/>
        </linearGradient>
        <linearGradient id="bandTone" x1="0" y1="0" x2="0" y2="1">
          <stop offset="0" stop-color="var(--brand-blue-dark)"/>
          <stop offset="1" stop-color="var(--brand-blue)"/>
        </linearGradient>
      </defs>
      <path role="img" aria-label="Photo of the trainer posing outdoors" d="M0 0 H180 Q290 150 215 309 H0 Z" fill="url(#photoTone)"/>
      <path class="curve-band" d="M180 0 Q290 150 215 309 L224 309 Q302 150 196 0 Z" fill="url(#bandTone)"/>
    </svg>

    <div class="contact">
      <h1 class="contact-name">Dorinda Pellham</h1>
      <p class="contact-phone">555-284-7163</p>
      <p class="contact-email">vetrubel4@quintmail.example</p>
    </div>

    <ul class="services">
      <li>Personal Fitness Trainer</li>
      <li>Sports Nutritionist</li>
      <li>Individual and Group rates available</li>
      <li>Certifications</li>
      <li>Global Wellness Coaching Federation</li>
      <li>Continental Athletic Studies Council</li>
    </ul>
  </section>

  <section class="card card-back">
    <p class="back-name">Dorinda Pellham</p>
  </section>
</body>
</html>
```